Pelinta Party Planning Brochure

I am beginning a new Party Planning business and need a brochure outlining my services. We are offering a full range of party/event-related planning services. These include Catering Halls/Restaurants, Photography/Video, International DJ's and Bands, Flowers, Tuxedos/Gowns, Limousines and Specialized Entertainers such as Clowns and Face Painters, Middle Eastern Belly Dancers, and Musical Impersonators (specifically, Dale Morrow impersonator). I would like a festive design, showing people having a good time in a festive setting. No vulgar or inappropriate photos or language, please.

Target Market(s)

Primarily, newly engaged couples. As for ethnic preference, Greek-speaking clientele.

Future brides, new parents and newly engaged couples, primarily in the Greek market.

Industry/Entity Type

Business

Font styles to use
Sans Serif

Colors
33a6d7

Requirements
Must have
• Mention of speaking Greek and Spanish. Festive design. I need to have this phrase included exactly as you see it
• I need the brochure to look, read and exude "happy".
Nice to have
• Pictures of party atmosphere. A lively room.
Should not have
• No vulgarities, no inappropriate pictures. No drunken photos or offensive images.

```html
<!DOCTYPE html>
<html lang="en">
<head>
<meta charset="utf-8">
<title>Pelinta Party Planning Brochure</title>
<link rel="stylesheet" href="https://fonts.googleapis.com/css2?family=Crimson+Pro:wght@600;700&family=Montserrat:wght@400;500;600&display=swap">
<style>
  :root {
    --brand-blue: #33a6d7;
    --brand-blue-deep: #1f86c0;
    --ink: #1a1a1a;
    --paper: #ffffff;
    --backdrop: #e9e6e2;
    --photo-warm-1: #d8c2a8;
    --photo-warm-2: #8a6e5a;
    --photo-food-1: #c9d98f;
    --photo-food-2: #e9b872;
  }
  * { margin: 0; padding: 0; box-sizing: border-box; }
  html, body { width: 1000px; height: 1200px; overflow: hidden; }
  body {
    position: relative;
    background: var(--backdrop);
    font-family: "Montserrat", Arial, sans-serif;
    color: var(--ink);
  }

  /* ---------- Front card ---------- */
  .card { position: absolute; background: var(--paper); }
  .card-front { left: 63px; top: 68px; width: 771px; height: 514px; }
  .card-front .front-art { position: absolute; inset: 0; }
  .front-title {
    font-family: "Crimson Pro", Georgia, serif;
    font-weight: 600;
    font-size: 39px;
    fill: var(--paper);
  }
  .front-footer {
    position: absolute; left: 0; right: 0; top: 456px;
    text-align: center; color: var(--brand-blue);
    font-size: 16.5px; line-height: 20px;
  }
  .front-footer strong { font-weight: 600; }

  /* ---------- Back card ---------- */
  .card-back { left: 168px; top: 633px; width: 772px; height: 514px; overflow: hidden; }
  .back-photo {
    position: absolute; left: 512px; top: 0; width: 260px; height: 514px;
    background:
      radial-gradient(ellipse at 40% 55%, var(--photo-food-2) 0%, transparent 45%),
      radial-gradient(ellipse at 60% 35%, var(--photo-food-1) 0%, transparent 55%),
      linear-gradient(180deg, #9fb2c4 0%, #c9cfa0 35%, #e6cf95 70%, #f1e2c4 100%);
  }
  .back-copy {
    position: absolute; left: 30px; top: 34px; width: 470px;
    text-align: center; font-size: 16.5px; line-height: 19.5px;
  }
  .back-heading {
    font-family: "Crimson Pro", Georgia, serif; font-weight: 700;
    font-size: 24px; line-height: 28px; color: var(--brand-blue);
    margin-bottom: 6px;
  }
  .back-copy p { margin-bottom: 6px; }
  .back-copy .accent { color: var(--brand-blue); font-weight: 600; }
  .languages {
    display: flex; justify-content: space-between;
    margin: 10px 14px 0 16px;
  }
  .closing-ribbon { position: absolute; left: 50px; top: 420px; width: 420px; height: 90px; }
  .closing-text { font-weight: 600; font-size: 18px; fill: var(--paper); }
</style>
</head>
<body>

<section class="card card-front">
  <svg class="front-art" viewBox="0 0 771 514" width="771" height="514">
    <defs>
      <linearGradient id="ribbonBlue" x1="0" x2="1" y1="0" y2="0">
        <stop offset="0" stop-color="var(--brand-blue-deep)"/>
        <stop offset="0.5" stop-color="var(--brand-blue)"/>
        <stop offset="1" stop-color="var(--brand-blue-deep)"/>
      </linearGradient>
      <radialGradient id="partyGlow" cx="0.75" cy="0.2" r="0.9">
        <stop offset="0" stop-color="#f4f1ee"/>
        <stop offset="0.35" stop-color="var(--photo-warm-1)"/>
        <stop offset="1" stop-color="var(--photo-warm-2)"/>
      </radialGradient>
    </defs>
    <path class="party-photo" role="img" aria-label="Photo of a group of friends laughing and singing into a microphone at a party"
      d="M66,80 C250,70 500,76 722,58 L712,432 C560,440 400,418 250,430 C180,436 120,428 72,436 Z"
      fill="url(#partyGlow)"/>
    <path class="side-ribbon" d="M42,62 L64,96 C58,200 62,330 80,432 C70,452 56,458 42,464 C38,330 36,200 42,62 Z" fill="url(#ribbonBlue)"/>
    <path class="title-ribbon" d="M42,62 C150,40 300,54 420,48 C550,42 650,18 740,26 L728,70 C640,62 540,80 420,86 C300,92 170,72 62,98 Z" fill="url(#ribbonBlue)"/>
    <text class="front-title" x="400" y="70" text-anchor="middle" transform="rotate(-2 400 60)">Pelinta Party Planning...</text>
  </svg>
  <div class="front-footer">
    Where Great Memories Are Waiting<br>
    Call Nina at <strong>(555) 214 7390</strong> or visit <strong>www.pelintapartyplanning.com</strong>
  </div>
</section>

<section class="card card-back">
  <div class="back-copy">
    <h2 class="back-heading">Pelinta Party Planning</h2>
    <p>is your only choice for complete party<br>and entertainment services</p>
    <p>Weddings, Birthdays, Anniversaries, Sweet 16s,<br>Quinceneras, Corporate events<br>or any event of any kind.</p>
    <p>We are ready to help you put together an<br>unforgettable experience for everyone<br>to remember</p>
    <p>We are affiliated with the best<br>catering halls &amp; restaurants, photo/video,<br>international DJs/bands, limos, wedding gowns<br>&amp; bridesmaids dresses, tuxedos, flowers, and<br>specialized entertainers</p>
    <p>Call us today at <span class="accent">(555) 214 7390</span> or<br>log on to <span class="accent">www.pelintapartyplanning.com</span></p>
    <div class="languages"><span>Hablamos Espanol</span><span>Milame Ellinika</span></div>
  </div>

  <svg class="closing-ribbon" viewBox="0 0 420 90" width="420" height="90">
    <path d="M18,30 C130,6 260,18 410,40 C395,55 392,70 398,86 C260,70 140,62 28,80 C10,72 4,56 8,44 C12,36 16,32 18,30 Z" fill="var(--brand-blue)"/>
    <text class="closing-text" x="210" y="44" text-anchor="middle" transform="rotate(4 210 44)">Let us make your special event</text>
    <text class="closing-text" x="218" y="67" text-anchor="middle" transform="rotate(4 218 67)">one that will last a lifetime!</text>
  </svg>

  <div class="back-photo" role="img" aria-label="Photo of a colourful buffet table with carved fruit and salads"></div>
</section>

</body>
</html>
```